CD-Cover und Booklet Gesprungen und geschnuppt
Punktgenaue Umsetzung unserer Wünsche, Verlässlichkeit und Genauigkeit. Der Designer hat von Beginn weg ein Grunddesign geliefert, das ansprechend war und dem Briefing entsprochen hat. In der Nachbearbeitung konnte dieses dann nach und nach zu einem sehr zufriedenstellenden Endergebnis verfeinert werden. Eine absolute Empfehlung!
Zielgruppe
Trompetenkreis Bad Ortmanning im Tal
www.trompetenkreis-ortmanning.example
Wir sind 15 Jagdhornbläser/Innen unterschiedlichen Alters (von 13-63 Jahre), die zurzeit ihre erste CD produzieren. Die Einspielung der CD hat bereits stattgefunden. Jetzt fehlt uns noch ein passendes Design.
Die Zielgruppe unserer CD ist grundsätzlich relativ exklusiv. Andere Jagdhornbläser, Horninteressierte, Jäger, hauptsächlich Altersgruppe 40+
Ziel ist es jedoch, mit einem frechen, neugierigen, modernen Design auch eine jüngere Altersgruppe anzusprechen.
Aufgabenstellung
Grundlayout des CD-Covers:
Farben und Stil unseres Logos verarbeiten: Weiß, Grün, Grau, Schrift schwarz, freundlich, hell, modern
Als Umschlag haben wir ausgewählt:
Digipak 6-seitig mit CD-Tray in der Mitte und Booklet-Schlitz rechts
COVER - Titelbild (Seite 3 - auf Druckvorlage rechts unten)
Titel der CD: "Gesprungen und g'schnuppt"
"Verhoffen" und "Lauschen" sind Begriffe der Jägersprache und lassen sich frei übersetzen in "Schauen/Innehalten" und "Hinhören". Wir haben deshalb als Titelbild ein Foto eines Rehbocks ausgewählt, der eben "verhofft und lauscht", also einen neugierigen, frechen und peppigen Blick zum Käufer richtet, dabei die Lauscher/Ohren aufgestellt. Unser Coverbild soll im wahrsten Sinne des Wortes ein Blickfang sein. Das Bild und der Titel sollen zum Hinschauen und Hinhören anregen.
Weiters sollen auf der ersten Seite der Titel der CD, unser Name "Trompetenkreis Bad Ortmanning/Tal" und unser Logo ohne darunterstehendem Schriftzug ersichtlich sein.
Seite 4 (einmal aufgeklappt - Druckvorlage rechts oben)
Gruppenfotos "1. Horn" und "2. Horn" mit folgenden Bildunterschriften:
zu "1. Horn": 1. Horn: Anton Brandstätter, Lukas Wunkel, Herbert Wunkel sen.
zu "2. Horn": 2. Horn: Renate Zoisl, Thomas Brandstätter, Florian Wunkel, Dominik Brandstätter
Seite 5 (CD-Tray - Druckvorlage oben mitte)
CD-Fach durchsichtig, Logo mit Schriftzug im Hintergrund
Seite 6 (Druckvorlage oben links)
Booklet-Tasche
Wenn Booklet herausgezogen wird, kommt Foto "Jagdhornbläser in Wiese" zum Vorschein
Seite 1 (Druckvorlage unten links)
Gruppenfotos "3. Horn" und "4. Horn"
Folgende Unterschriften:
zu "3. Horn": 3. Horn: Eva Pichlmayr, Rudolf Zoisl, Karl Brandstätter, Veronika Stadlbauer
zu "4. Horn": Andreas Lechner, Andreas Wunkel, Herbert Wunkel jun., Gernot Brandstätter
Seite 2 (Druckvorlage unten mitte)
Rückseite (Stückliste, Impress..

```html
<!DOCTYPE html>
<html lang="de">
<head>
<meta charset="utf-8">
<title>Gesprungen und g'schnuppt – CD-Digipak und Booklet</title>
<link rel="stylesheet" href="https://fonts.googleapis.com/css2?family=Josefin+Sans:wght@600;700&family=Dancing+Script:wght@600&family=Roboto+Condensed:wght@400;700&family=Cinzel:wght@500&display=swap">
<style>
  :root {
    --bg: #e3e3e3;
    --paper: #f6f6f4;
    --green: #3f7d3c;
    --green-soft: #9cc28a;
    --box: rgba(52, 84, 66, 0.86);
    --ink: #2b2b2b;
    --grey-text: #7a7a7a;
    --caption: rgba(30, 40, 32, 0.75);
  }
  * { box-sizing: border-box; margin: 0; padding: 0; }
  html, body { width: 1200px; height: 2426px; overflow: hidden; }
  body { background: var(--bg); position: relative; font-family: 'Roboto Condensed', sans-serif; color: var(--ink); }

  .panel { position: absolute; overflow: hidden; box-shadow: 0 6px 18px rgba(0,0,0,0.18); background: var(--paper); }
  .photo { position: absolute; }

  /* Front cover */
  .cover-front { left: 40px; top: 150px; width: 540px; height: 540px; }
  .cover-front .photo { inset: 0; background:
      radial-gradient(ellipse 46% 40% at 50% 92%, #7d6a55 0%, #8f7d66 45%, rgba(143,125,102,0) 100%),
      radial-gradient(ellipse 30% 34% at 30% 62%, rgba(150,128,104,0.85) 0%, rgba(150,128,104,0) 100%),
      radial-gradient(ellipse 26% 34% at 74% 58%, rgba(150,128,104,0.85) 0%, rgba(150,128,104,0) 100%),
      linear-gradient(160deg, #cfe0bd 0%, #b3cf95 40%, #93b86c 100%); }
  .title-block { position: absolute; left: 0; right: 0; top: 40px; text-align: center; }
  .title-club { font-family: 'Dancing Script', cursive; color: var(--green); font-size: 22px; }
  .title-main { font-family: 'Josefin Sans', sans-serif; font-weight: 700; font-size: 46px; letter-spacing: 2px; color: #333; line-height: 1; }
  .title-und { font-family: 'Dancing Script', cursive; font-size: 16px; color: var(--green); line-height: 1; margin: 2px 0; }
  .title-rule { width: 260px; height: 2px; background: var(--green); margin: 4px auto; }

  /* Back cover */
  .cover-back { left: 620px; top: 150px; width: 540px; height: 540px; }
  .cover-back .photo { inset: 0; background:
      radial-gradient(ellipse 12% 26% at 32% 52%, rgba(70,82,52,0.75) 0%, rgba(70,82,52,0) 100%),
      radial-gradient(ellipse 8% 20% at 12% 56%, rgba(70,82,52,0.6) 0%, rgba(70,82,52,0) 100%),
      linear-gradient(180deg, #a9c3dc 0%, #dfe7ea 30%, #c6d27a 44%, #b5c652 70%, #9fb43f 100%); }
  .info-box { position: absolute; left: 262px; top: 24px; width: 256px; height: 372px; background: var(--box); color: #fff; padding: 16px; }
  .info-box h2 { font-family: 'Josefin Sans', sans-serif; font-size: 14px; letter-spacing: 1px; font-weight: 700; margin-bottom: 8px; }
  .tracks { list-style: none; font-size: 10px; line-height: 14px; }
  .tracks li { display: flex; gap: 4px; }
  .tracks .dots { flex: 1; border-bottom: 1px dotted rgba(255,255,255,0.7); margin-bottom: 4px; }
  .info-box p { font-size: 8px; line-height: 11px; margin-top: 10px; text-transform: uppercase; }
  .contact { font-size: 7px; line-height: 10px; margin-top: 8px; text-transform: uppercase; }
  .brand { display: flex; align-items: center; gap: 6px; justify-content: center; margin-top: 12px; font-family: 'Cinzel', serif; font-size: 9px; }
  .brand .dot { width: 10px; height: 10px; border-radius: 50%; background: currentColor; }

  /* Digipak inside */
  .digi { top: 950px; width: 370px; height: 370px; }
  .digi-left { left: 30px; }
  .digi-mid { left: 415px; background: #d8d8d6; }
  .digi-right { left: 800px; }
  .digi .photo { left: 0; right: 0; }
  .ph-top { top: 0; height: 160px; background: linear-gradient(180deg, #7d9a5e 0%, #5d7a45 35%, #2f4b33 60%, #e4e2da 78%, #6f8752 100%); }
  .ph-bottom { top: 166px; height: 204px; background: linear-gradient(180deg, #5f7f46 0%, #3e5b36 30%, #2c452c 55%, #dcd6c8 72%, #587a41 100%); }
  .caption { position: absolute; left: 0; right: 0; background: var(--caption); color: #fff; font-size: 7px; font-weight: 700; letter-spacing: 0.2px; text-transform: uppercase; padding: 4px 8px; white-space: nowrap; }
  .caption.top { top: 8px; text-align: right; }
  .caption.bottom { bottom: 8px; }
  .tray { position: absolute; inset: 22px; border-radius: 10px; background: linear-gradient(180deg, #e6e6e4, #cfcfcc); }
  .cd { position: absolute; left: 45px; top: 45px; width: 280px; height: 280px; border-radius: 50%; background: #f7f7f3; box-shadow: 0 2px 6px rgba(0,0,0,0.2); }
  .cd-hub { position: absolute; left: 105px; top: 105px; width: 70px; height: 70px; border-radius: 50%; background: #bdbdbb; border: 6px solid #d9d9d7; }
  .cd-hole { position: absolute; left: 125px; top: 125px; width: 30px; height: 30px; border-radius: 50%; background: #e8e8e6; }
  .cd-name { position: absolute; left: 0; right: 0; top: 48px; text-align: center; font-family: 'Cinzel', serif; color: #333; }
  .cd-name .n1 { font-size: 18px; letter-spacing: 1px; }
  .cd-name .n2 { font-size: 10px; color: var(--green); }
  .cd-title { position: absolute; left: 0; right: 0; bottom: 58px; text-align: center; font-family: 'Josefin Sans', sans-serif; font-weight: 700; font-size: 13px; color: var(--green); letter-spacing: 1px; }

  /* Booklet */
  .spread { position: absolute; width: 540px; height: 270px; display: flex; box-shadow: 0 6px 18px rgba(0,0,0,0.18); }
  .page { position: relative; width: 270px; height: 270px; background: var(--paper); overflow: hidden; }
  .page + .page { border-left: 1px solid #dcdcda; }
  .spread-a { left: 40px; top: 1560px; }
  .spread-b { left: 620px; top: 1830px; }
  .spread-c { left: 40px; top: 2100px; }
  .head-rule { position: absolute; top: 18px; left: 18px; right: 18px; height: 1px; background: var(--green-soft); }
  .head-mark { position: absolute; top: 13px; left: 129px; width: 12px; height: 12px; border-radius: 50%; border: 1px solid var(--green); background: var(--paper); }
  .foot { position: absolute; bottom: 14px; left: 18px; right: 18px; text-align: center; font-size: 7px; font-weight: 700; color: var(--green); letter-spacing: 0.5px; text-transform: uppercase; display: flex; align-items: center; gap: 6px; white-space: nowrap; }
  .foot::before, .foot::after { content: ""; flex: 1; height: 1px; background: var(--green-soft); }
  .body-text { position: absolute; font-size: 6px; line-height: 9px; text-transform: uppercase; color: var(--grey-text); }
  .body-text p + p { margin-top: 8px; }
  .portrait { position: absolute; left: 28px; top: 50px; width: 70px; height: 80px; background: #a9a9a9; }
  .signee { position: absolute; left: 12px; top: 138px; width: 100px; text-align: right; font-size: 5.5px; line-height: 8px; color: var(--green); text-transform: uppercase; }
  .greeting { font-weight: 700; color: #555; }
  .sign { font-family: 'Dancing Script', cursive; font-size: 9px; color: var(--green); text-transform: none; }
  .page-photo { position: absolute; inset: 0; background:
      radial-gradient(ellipse 45% 18% at 40% 62%, rgba(60,66,44,0.7) 0%, rgba(60,66,44,0) 100%),
      linear-gradient(180deg, #c9dc8e 0%, #94b954 35%, #6f9a3e 65%, #4f7230 100%); }
  .page-box { position: absolute; right: 18px; top: 22px; width: 120px; height: 130px; background: var(--box); color: #fff; padding: 8px; font-size: 5.5px; line-height: 8px; text-transform: uppercase; }
  .page-box .brand { margin: 0 0 8px; font-size: 6px; }
  .group-photo { position: absolute; inset: 0; background:
      linear-gradient(180deg, #6c8a52 0%, #8f9a7c 20%, #c9c1b0 34%, #35503a 52%, #2e4630 68%, #8a8e72 84%, #6b7a58 100%); }
  .group-brand { position: absolute; right: 30px; bottom: 22px; color: #fff; font-family: 'Cinzel', serif; font-size: 11px; display: flex; align-items: center; gap: 6px; }
  .group-brand .dot { width: 12px; height: 12px; border-radius: 50%; border: 1.5px solid #fff; }
</style>
</head>
<body>

<section class="panel cover-front">
  <div class="photo" role="img" aria-label="Nahaufnahme eines Rehbocks mit aufgestellten Lauschern vor grünem Hintergrund"></div>
  <div class="title-block">
    <div class="title-club">Trompetenkreis Bad Ortmanning/Tal</div>
    <div class="title-main">GESPRUNGEN</div>
    <div class="title-und">und</div>
    <div class="title-rule"></div>
    <div class="title-main">G'SCHNUPPT</div>
  </div>
</section>

<section class="panel cover-back">
  <div class="photo" role="img" aria-label="Zwei Jagdhornbläser gehen durch eine hohe Sommerwiese unter blauem Himmel"></div>
  <div class="info-box">
    <h2>GESPRUNGEN &amp; G'SCHNUPPT</h2>
    <ol class="tracks">
      <li>01 Titel<span class="dots"></span>2:46</li>
      <li>02 Titel<span class="dots"></span>3:33</li>
      <li>03 Titel<span class="dots"></span>1:59</li>
      <li>04 Titel<span class="dots"></span>5:27</li>
      <li>05 Titel<span class="dots"></span>1:23</li>
      <li>06 Titel<span class="dots"></span>3:33</li>
      <li>07 Titel<span class="dots"></span>3:33</li>
      <li>08 Titel<span class="dots"></span>5:27</li>
      <li>09 Titel<span class="dots"></span>5:27</li>
      <li>10 Titel<span class="dots"></span>3:33</li>
      <li>11 Titel<span class="dots"></span>3:33</li>
      <li>12 Titel<span class="dots"></span>5:27</li>
    </ol>
    <p>Zwölf Stücke für Jagdhorn, aufgenommen im Frühjahr im Tal. Hören, schauen, innehalten.</p>
    <div class="contact">
      Trompetenkreis Bad Ortmanning/Tal<br>
      Tel. +43 0000 00000<br>
      E-Mail: info@trompetenkreis-ortmanning.example<br>
      www.trompetenkreis-ortmanning.example
    </div>
    <div class="brand"><span class="dot"></span>Trompetenkreis</div>
  </div>
</section>

<section class="panel digi digi-left">
  <div class="photo ph-top" role="img" aria-label="Gruppenfoto der Bläser des 1. Horns in Tracht"></div>
  <div class="caption top">1. Horn / Anton Brandstätter / Lukas Wunkel / Herbert Wunkel sen.</div>
  <div class="photo ph-bottom" role="img" aria-label="Gruppenfoto der Bläser des 2. Horns im Wald"></div>
  <div class="caption bottom">2. Horn / Renate Zoisl / Thomas Brandstätter / Florian Wunkel / Dominik Brandstätter</div>
</section>

<section class="panel digi digi-mid">
  <div class="tray"></div>
  <div class="cd">
    <div class="cd-name"><div class="n1">TROMPETENKREIS</div><div class="n2">BAD ORTMANNING IM TALE</div></div>
    <div class="cd-hub"></div>
    <div class="cd-hole"></div>
    <div class="cd-title">GESPRUNGEN &amp; GESCHNUPPT</div>
  </div>
</section>

<section class="panel digi digi-right">
  <div class="photo ph-top" role="img" aria-label="Gruppenfoto der Bläser des 3. Horns in Tracht"></div>
  <div class="caption top">3. Horn / Eva Pichlmayr / Rudolf Zoisl / Karl Brandstätter / Veronika Stadlbauer</div>
  <div class="photo ph-bottom" role="img" aria-label="Gruppenfoto der Bläser des 4. Horns auf einer Wiese"></div>
  <div class="caption bottom">4. Horn / Andreas Lechner / Andreas Wunkel / Herbert Wunkel jun. / Gernot Brandstätter</div>
</section>

<section class="spread spread-a">
  <div class="page">
    <div class="head-rule"></div><div class="head-mark"></div>
    <div class="portrait" role="img" aria-label="Platzhalter für das Porträt des Bürgermeisters"></div>
    <div class="signee">Hans Beispielmann<br>Bürgermeister Bad Ortmanning/Tal</div>
    <div class="body-text" style="left:124px; top:48px; width:128px;">
      <p class="greeting">Servus und Grüß Gott!</p>
      <p>Es freut mich sehr, dass unser Trompetenkreis nun seine erste CD vorlegt. Viele Stunden Probe und Hingabe stecken in jedem Stück.</p>
      <p>Viel Freude beim Hören!</p>
      <p class="sign">Gesprungen und g'schnuppt</p>
    </div>
    <div class="foot">Gesprungen &amp; Geschnuppt</div>
  </div>
  <div class="page">
    <div class="head-rule"></div>
    <div class="body-text" style="left:22px; top:34px; width:200px;">
      <p>Seit vielen Jahren pflegen wir das Blasen auf dem Jagdhorn im Tal. Bei Festen, Messen und Jagden begleiten wir die Menschen unserer Gemeinde.</p>
      <p>Die jüngsten Mitglieder sind dreizehn, die ältesten über sechzig. Gemeinsam proben wir jede Woche im Vereinshaus.</p>
    </div>
    <div class="foot">Trompetenkreis Bad Ortmanning/Tal</div>
  </div>
</section>

<section class="spread spread-b">
  <div class="page">
    <div class="head-rule"></div><div class="head-mark"></div>
    <div class="body-text" style="left:22px; top:40px; width:210px;">
      <p>Die Aufnahmen entstanden an mehreren Abenden im Frühling. Jedes Stück wurde im Freien geprobt.</p>
      <p>Unser Dank gilt allen Helfern, Familien und Freunden, die uns dabei unterstützt haben.</p>
    </div>
    <div class="foot">Gesprungen &amp; Geschnuppt</div>
  </div>
  <div class="page">
    <div class="page-photo" role="img" aria-label="Jagdhornbläser liegt mit seinem Horn im hohen Gras"></div>
    <div class="page-box">
      <div class="brand"><span class="dot"></span>Trompetenkreis</div>
      Im hohen Gras ruht der Bläser und lauscht dem Wind. So klingt für uns der Sommer.
    </div>
  </div>
</section>

<section class="spread spread-c">
  <div class="page" style="width:540px;">
    <div class="group-photo" role="img" aria-label="Gruppenfoto aller Bläserinnen und Bläser in Tracht vor einer steinernen Kapelle"></div>
    <div class="group-brand"><span class="dot"></span>Trompetenkreis</div>
  </div>
</section>

</body>
</html>
```